Billboard design 8x3M NURA (Spanish company)

We´re located in the south of Spain. We run a local telecom company.
We sell Fiber optic, and mobile phone lines mainly.
The billboard will have to be in Spanish, I would like the price to be something you spot on first sight when passing by in the car.
Our company color is blue, like in our logo which I will add. I will also add a example from what we currently have.
The new offer should be:
1000 megas + 100Gigas movil con llamadas ilimitadas. (meaning 1000Mb fiber optic speed and 100Gb data and unlimited calls for 1 mobile line)
Our details are: phone line 952 00 0147
Website: nu-ra.es

```html
<!DOCTYPE html>
<html lang="es">
<head>
<meta charset="utf-8">
<title>NURA – Valla 8x3</title>
<link href="https://fonts.googleapis.com/css2?family=Poppins:wght@500;600;700&display=swap" rel="stylesheet">
<style>
  :root {
    --blue-light: #2a9fd6;
    --blue-deep: #17698f;
    --blue-brand: #2596cf;
    --navy: #1c3550;
    --gold: #e0ab2e;
    --white: #ffffff;
    --stage: #e9edf2;
  }
  * { margin: 0; padding: 0; box-sizing: border-box; }
  html, body { width: 1200px; height: 780px; overflow: hidden; }
  body {
    background: var(--stage);
    font-family: "Poppins", sans-serif;
    position: relative;
  }
  .billboard {
    position: absolute;
    left: 0; top: 165px;
    width: 1200px; height: 450px;
    overflow: hidden;
    background: linear-gradient(100deg, var(--blue-light) 0%, var(--blue-deep) 70%);
  }
  .billboard__white { position: absolute; inset: 0; }
  .offer { position: absolute; left: 30px; top: 20px; width: 330px; color: var(--white); text-align: center; }
  .offer__speed { font-size: 130px; font-weight: 700; line-height: 1; letter-spacing: -3px; }
  .offer__unit {
    display: block; margin: 4px auto 0; width: 310px;
    background: var(--gold); border-radius: 12px;
    font-size: 52px; font-weight: 600; line-height: 70px;
  }
  .offer__data { font-size: 80px; font-weight: 700; line-height: 1.05; letter-spacing: -3px; margin-top: 6px; white-space: nowrap; }
  .offer__calls { font-size: 29px; font-weight: 500; line-height: 1.15; white-space: nowrap; }
  .arrow { position: absolute; left: 360px; top: 55px; }
  .price {
    position: absolute; left: 372px; top: 218px;
    width: 165px; height: 165px; border-radius: 50%;
    background: var(--gold); color: var(--white);
    display: flex; flex-direction: column; align-items: center; justify-content: center;
    z-index: 2;
  }
  .price__label { font-size: 28px; font-weight: 500; line-height: 1; }
  .price__amount { font-size: 66px; font-weight: 600; line-height: 1; letter-spacing: -2px; }
  .photo {
    position: absolute; left: 545px; top: 100px; width: 295px; height: 350px;
    background: linear-gradient(180deg, #bcc9d8 0%, #cfd6df 45%, #8a5a36 78%, #6e4426 100%);
    border-radius: 4px 4px 0 0;
  }
  .brand { position: absolute; left: 862px; top: 60px; width: 320px; color: var(--navy); }
  .brand__name { font-size: 84px; font-weight: 700; color: var(--blue-brand); line-height: 1; letter-spacing: 2px; }
  .brand__services { font-size: 24px; font-weight: 500; color: var(--blue-brand); margin-top: 6px; white-space: nowrap; }
  .brand__phone { font-size: 44px; font-weight: 700; line-height: 1.1; margin-top: 28px; white-space: nowrap; }
  .brand__web { font-size: 38px; font-weight: 700; line-height: 1.1; white-space: nowrap; }
  .brand__bar { width: 230px; height: 24px; background: var(--gold); border-radius: 12px; margin-top: 28px; }
</style>
</head>
<body>
  <section class="billboard">
    <svg class="billboard__white" width="1200" height="450" viewBox="0 0 1200 450" aria-hidden="true">
      <path d="M930,0 C790,60 700,170 690,450 L1200,450 L1200,0 Z" fill="#ffffff"/>
    </svg>

    <div class="offer">
      <div class="offer__speed">1000</div>
      <span class="offer__unit">MEGAS</span>
      <div class="offer__data">+ 100Gb</div>
      <p class="offer__calls">movil con llamadas<br>ilimitadas</p>
    </div>

    <svg class="arrow" width="120" height="150" viewBox="0 0 120 150" aria-hidden="true">
      <path d="M5,22 C60,0 100,30 98,118" fill="none" stroke="#0d1a26" stroke-width="4"/>
      <path d="M84,108 L98,136 L110,106 Z" fill="#0d1a26"/>
    </svg>

    <div class="photo" role="img" aria-label="Foto de un hombre con gafas y casco de aviador, puño en alto, sentado ante un portátil en una mesa de madera con zumo y cactus"></div>

    <div class="price">
      <span class="price__label">por</span>
      <span class="price__amount">35€</span>
    </div>

    <div class="brand">
      <div class="brand__name">NURA</div>
      <div class="brand__services">Wifi | Fibra | Movil | Tv</div>
      <div class="brand__phone">952 00 0147</div>
      <div class="brand__web">www.nu-ra.es</div>
      <div class="brand__bar"></div>
    </div>
  </section>
</body>
</html>
```